PELDRAX Business Cards

We require a business card for our company that provides IT consulting services. We already have a logo that needs to be used on the card. We want a clean professional looking design that incorporates our colours. Our main focus is providing managed services to business, which involves us looking after all of their IT requirements including managing servers/networks, projects, and procurement.

Industry/Entity Type

Information Technology

Requirements
Must have
• our logo, contact information, name, title, phone numbers

```html
<!DOCTYPE html>
<html lang="en">
<head>
<meta charset="utf-8">
<title>PELDRAX Business Cards</title>
<link rel="stylesheet" href="https://fonts.googleapis.com/css2?family=Lato:wght@400;700;900&family=Roboto:wght@400&display=swap">
<style>
  :root {
    --backdrop: #3b3b3d;
    --brand-blue: #1596cf;
    --card-white: #f4f4f4;
    --ink: #474747;
    --white: #ffffff;
  }
  * { margin: 0; padding: 0; box-sizing: border-box; }
  html, body { width: 1200px; height: 960px; overflow: hidden; }
  body {
    background: var(--backdrop);
    position: relative;
    font-family: "Roboto", Arial, sans-serif;
  }
  .card {
    position: absolute;
    width: 600px;
    height: 343px;
  }
  .card--front { left: 314px; top: 113px; background: var(--card-white); }
  .card--back { left: 311px; top: 472px; background: var(--brand-blue); }

  .name-band {
    position: absolute;
    left: 0; top: 40px;
    width: 330px; height: 67px;
    background: var(--brand-blue);
    clip-path: polygon(0 0, 100% 0, 93% 100%, 0 100%);
  }
  .holder-name {
    position: absolute;
    left: 36px; top: 57px;
    font-family: "Lato", Arial, sans-serif;
    font-weight: 700;
    font-size: 22px;
    color: var(--white);
    letter-spacing: 0.3px;
  }
  .holder-title {
    position: absolute;
    left: 37px; top: 83px;
    font-family: "Lato", Arial, sans-serif;
    font-weight: 700;
    font-size: 14.5px;
    color: var(--white);
  }
  .brand-name {
    position: absolute;
    right: 37px; top: 56px;
    font-family: "Lato", Arial, sans-serif;
    font-weight: 700;
    font-size: 42px;
    line-height: 1;
    letter-spacing: 1px;
    color: var(--brand-blue);
  }
  .contact-list {
    position: absolute;
    left: 38px; top: 228px;
    list-style: none;
  }
  .contact-list li {
    display: flex;
    align-items: center;
    height: 19px;
    font-size: 14px;
    color: var(--ink);
  }
  .contact-list svg {
    width: 14px; height: 14px;
    margin-right: 8px;
    fill: var(--brand-blue);
  }
  .address {
    position: absolute;
    right: 37px; top: 252px;
    text-align: right;
    font-size: 14px;
    line-height: 18.5px;
    color: var(--ink);
  }
  .address .web { letter-spacing: 1.6px; }

  .back-brand {
    position: absolute;
    left: 0; right: 0; top: 140px;
    text-align: center;
    font-family: "Lato", Arial, sans-serif;
    font-weight: 700;
    font-size: 58px;
    letter-spacing: 2px;
    color: var(--white);
  }
  .back-web {
    position: absolute;
    left: 0; right: 0; top: 298px;
    text-align: center;
    font-size: 14px;
    letter-spacing: 5.5px;
    color: var(--white);
  }
</style>
</head>
<body>
  <section class="card card--front">
    <div class="name-band"></div>
    <div class="holder-name">MARTIN HALE</div>
    <div class="holder-title">CEO/FOUNDER</div>
    <div class="brand-name">PELDRAX</div>

    <ul class="contact-list">
      <li><svg viewBox="0 0 14 14"><path d="M3 1l2.2 2.6-1.3 1.6c.9 1.9 2.3 3.3 4.2 4.2l1.6-1.3L12.3 10.3 11 12.8C5.6 12.5 1.5 8.4 1.2 3z"/></svg>614 275 3081</li>
      <li><svg viewBox="0 0 14 14"><path d="M4 0h6a1 1 0 0 1 1 1v12a1 1 0 0 1-1 1H4a1 1 0 0 1-1-1V1a1 1 0 0 1 1-1zm.5 1.5v9.5h5V1.5zM7 11.6a.8.8 0 1 0 0 1.6.8.8 0 0 0 0-1.6z"/></svg>752 319 4826</li>
      <li><svg viewBox="0 0 14 14"><path d="M3 1h8v3H3zM1 5h12v6h-2V9H3v2H1zM3.5 10h7v3h-7z"/></svg>503 781 2469</li>
      <li><svg viewBox="0 0 14 14"><path d="M1 3h12v8H1zm1.2 1.1L7 7.6l4.8-3.5v-.1H2.2z"/></svg>martin@peldrax.com</li>
    </ul>

    <div class="address">
      <div>4120 Birchwood Court</div>
      <div>Fairbanks, Alaska 39810</div>
      <div class="web">www.peldrax.com</div>
    </div>
  </section>

  <section class="card card--back">
    <div class="back-brand">PELDRAX</div>
    <div class="back-web">www.peldrax.com</div>
  </section>
</body>
</html>
```